Flyer Required for Economics Tuition business in Singapore

Require a 4-page, A4 bi-fold full colour flyer. To use attractive & vibrant colours. Can make use of colour schemes and design layouts from upcoming website revamp: http://lessonbrightpath.com/Website/
Target audience for the flyer will be 17 - 18 years old A Level students in Singapore studying in Junior Colleges.
I have attached the detailed design brief with the content required for the flyer as a file titled "Design Brief.docx" & also the logo for our business to be used in the flyer & optional photos that can be used in the flyer
Reason: Require more designs. Current designs provided are too "template" like

```html
<!DOCTYPE html>
<html lang="en">
<head>
<meta charset="utf-8">
<title>Lesson Brightpath – Economics Tuition Flyer</title>
<link rel="stylesheet" href="https://fonts.googleapis.com/css2?family=Questrial&family=Didact+Gothic&display=swap">
<style>
:root{
  --orange:#f7941d;
  --orange-deep:#ef7f1a;
  --charcoal:#3b3b3d;
  --ink:#4a4a4a;
  --cream:#fdf7ee;
  --line:#bdb6ab;
  --stage:#e6e6e6;
  --photo-a:#8fb3d6;
  --photo-b:#dfe7ef;
}
*{box-sizing:border-box;margin:0;padding:0}
html,body{width:1200px;height:1000px;overflow:hidden}
body{background:var(--stage);font-family:"Didact Gothic","Questrial",sans-serif;color:var(--ink);position:relative}
.page{position:absolute;width:340px;height:481px;background:var(--cream);overflow:hidden;box-shadow:0 2px 8px rgba(0,0,0,.18)}
.spread-left{left:30px;top:259px}
.spread-right{left:370px;top:259px;border-left:1px solid #e2d9cb}
.cover{left:800px;top:10px}
.back{left:800px;top:509px}
.photo{position:absolute;background:linear-gradient(160deg,var(--photo-b),var(--photo-a))}
p,.txt{font-size:5.6px;line-height:1.35}
.tag{position:absolute;display:inline-block;background:var(--orange);color:#fff;font-family:"Questrial",sans-serif;font-size:8px;line-height:1.2;padding:2px 6px}
.tag.dark{background:var(--charcoal)}
.label-box{position:absolute;background:#fff;border:1px solid var(--charcoal);font-family:"Questrial",sans-serif;font-size:10px;padding:3px 8px;color:var(--charcoal)}
.label-box b{color:var(--orange);font-weight:400}
.section{position:absolute}
.section p{margin-top:3px}
.name-tag{display:inline-block;font-size:5.5px;margin:3px 0 2px}
.name-tag span:first-child{background:var(--orange);color:#fff;padding:1px 3px}
.name-tag span:last-child{border:1px solid var(--charcoal);padding:0 3px;margin-left:2px}
/* cover */
.cover-head{position:absolute;left:0;top:0;width:340px;height:82px}
.brand{position:absolute;left:16px;top:30px;display:flex;align-items:center;gap:5px;font-family:"Questrial",sans-serif;color:var(--orange);font-size:13px}
.brand i{width:9px;height:9px;border-radius:50%;background:var(--orange);display:block}
.cover-title{position:absolute;left:168px;top:14px;width:166px;text-align:right}
.cover-title h1{font-family:"Questrial",sans-serif;font-weight:400;font-size:17px;color:#fff}
.cover-title h2{font-family:"Questrial",sans-serif;font-weight:400;font-size:9px;color:var(--charcoal);line-height:1.25;margin-top:3px}
.intro{position:absolute;top:88px;width:150px}
.intro h3{font-family:"Questrial",sans-serif;font-weight:400;font-size:7px;color:var(--orange)}
.ribbon{position:absolute;left:90px;top:150px;width:190px;height:13px;background:var(--charcoal);color:#fff;font-family:"Questrial",sans-serif;font-size:7px;text-align:center;line-height:13px}
.ribbon b{color:var(--orange);font-weight:400}
.results{position:absolute;top:168px;width:100px;border-collapse:collapse;font-size:4.6px}
.results td{border:1px solid var(--line);padding:0 2px;height:9.4px;background:#fff}
.results td:last-child{text-align:center;width:12px}
.cover-foot{position:absolute;left:0;top:400px;width:340px;height:81px;background:var(--orange);color:#fff}
.cover-foot p{position:absolute;top:8px;width:150px;color:#fff;font-size:5.2px}
.cover-foot .tag{top:60px}
/* back */
.back-band{position:absolute;left:0;top:0;width:340px;height:150px;background:var(--orange)}
.sched{position:absolute;top:176px;width:148px;border-collapse:collapse;font-size:5.2px;background:#fff}
.sched td{border:1px solid var(--charcoal);padding:1px 2px;height:11px}
.locations{position:absolute;left:30px;top:306px;width:280px;height:76px;border:1px solid var(--orange);padding:8px 10px;display:grid;grid-template-columns:1fr 1fr;gap:5px 14px}
.loc h4{font-family:"Questrial",sans-serif;font-weight:400;font-size:7px;color:var(--orange)}
.loc p{font-size:5.3px}
.fees{position:absolute;left:0;top:404px;width:340px;text-align:center;font-family:"Questrial",sans-serif;color:var(--charcoal)}
.fees .line{font-size:7.5px;line-height:1.3}
.fees .call{font-size:10px;margin-top:5px}
.fees .call b{color:#fff;background:var(--orange);font-weight:400;padding:0 3px}
</style>
</head>
<body>

<!-- Inside spread: founder page -->
<section class="page spread-left" aria-label="About our programme founder">
  <div class="photo" style="left:0;top:0;width:340px;height:175px" role="img" aria-label="Group photo of tuition students"></div>
  <div class="label-box" style="left:150px;top:166px">About our Programme <b>Founder</b></div>

  <div class="photo" style="left:232px;top:196px;width:92px;height:82px;background:linear-gradient(160deg,#f2f2f2,#b9b9b9)" role="img" aria-label="Portrait of the programme founder"></div>
  <div class="photo" style="left:232px;top:286px;width:92px;height:62px" role="img" aria-label="Founder teaching a class"></div>

  <div class="section" style="left:14px;top:196px;width:210px">
    <span class="tag" style="position:static">Background</span>
    <p>Mr Lim is the Programme Founder and Managing Director of Lesson Brightpath. He graduated with a degree in Economics and holds teaching credentials from a leading local institute.</p>
  </div>
  <div class="section" style="left:14px;top:248px;width:210px">
    <span class="tag" style="position:static">Academic Qualifications</span>
    <p>He holds an Honours degree in Economics and a Master's in Finance, and has trained with national examiners on A Level marking standards.</p>
  </div>
  <div class="section" style="left:14px;top:296px;width:210px">
    <span class="tag" style="position:static">Teaching Experience</span>
    <p>Mr Lim has taught A Level Economics for over ten years, guiding more than 2000 students to strong results across many junior colleges.</p>
  </div>
  <div class="section" style="left:14px;top:362px;width:312px">
    <span class="tag" style="position:static">Style of Teaching</span>
    <p>Mr Lim is different from other tutors because he uses a mixture of strategies to help the student excel. He breaks down each topic into clear frameworks, uses real world cases, and trains students to write essays that score. Lessons are lively, structured and focused on exam skills, so students build confidence and steady progress through the year.</p>
  </div>
</section>

<!-- Inside spread: testimonials page -->
<section class="page spread-right" aria-label="Testimonials from students">
  <div class="photo" style="left:0;top:0;width:340px;height:150px" role="img" aria-label="Students posing together in class"></div>
  <div class="label-box" style="left:92px;top:140px">Testimonials <b>From Students</b></div>

  <div class="section" style="left:14px;top:172px;width:148px">
    <p>Mr Lim really has all his students' interests at heart. His notes are clear and his lessons are easy to follow.</p>
    <div class="name-tag"><span>Rachel Tan</span><span>Harbourview JC</span></div>
    <p>He explains difficult concepts simply and always makes time for our questions after class.</p>
    <div class="name-tag"><span>Daniel Koh</span><span>Cedar Hill Institution</span></div>
    <p>The essay frameworks helped me go from a U grade to an A within a year. Thank you!</p>
    <div class="name-tag"><span>Priya Nair</span><span>Northgate JC</span></div>
    <p>Lessons were fun and engaging and I looked forward to every class.</p>
    <div class="name-tag"><span>Marcus Ong</span><span>Cedar Hill Institution</span></div>
  </div>
  <div class="section" style="left:176px;top:172px;width:150px">
    <p>Mr Lim and the tuition centre have greatly improved my grades. The materials are concise and well organised.</p>
    <div class="name-tag"><span>Jia Hui Lee</span><span>Harbourview JC</span></div>
    <p>He is very patient and genuinely cares. I gained real confidence before my exams.</p>
    <div class="name-tag"><span>Aaron Goh</span><span>Cedar Hill Institution</span></div>
    <p>Mr Lim is a committed tutor who goes the extra mile to help each of us understand the topic.</p>
    <div class="name-tag"><span>Nicole Chua</span><span>Cedar Hill Institution</span></div>
    <p>Highly recommended for anyone struggling with case studies.</p>
    <div class="name-tag"><span>Ethan Wee</span><span>Northgate JC</span></div>
  </div>
  <div class="photo" style="left:14px;top:402px;width:148px;height:68px" role="img" aria-label="Lecture room full of students"></div>
  <div class="photo" style="left:176px;top:402px;width:150px;height:68px" role="img" aria-label="Students working in class"></div>
</section>

<!-- Front cover -->
<section class="page cover" aria-label="Front cover">
  <svg class="cover-head" viewBox="0 0 340 82" aria-hidden="true">
    <rect width="340" height="82" fill="#f7941d"/>
    <polygon points="0,0 165,0 140,82 0,82" fill="#3b3b3d"/>
  </svg>
  <div class="brand"><i></i>Lesson Brightpath</div>
  <div class="cover-title">
    <h1>Failing Economics?</h1>
    <h2>It's time to get the RIGHT help<br>for your A Level Economics!</h2>
  </div>

  <div class="intro" style="left:14px">
    <h3>Singapore's Leading Economics Tuition Programme</h3>
    <p>The Economics tuition programme is designed to help A Level students master concepts and exam skills. Classes are taught by Mr Lim, founder of Lesson Brightpath.</p>
  </div>
  <div class="intro" style="left:178px">
    <h3>Why join us?</h3>
    <p>Since 2010, Mr Lim has been teaching hundreds of students each year. Over 80% of our students scored A or B in the latest A Level examinations.</p>
  </div>

  <div class="ribbon"><b>Congratulations</b> to the following students!</div>

  <table class="results" style="left:12px"><tbody>
    <tr><td>Rachel Tan</td><td>A</td></tr><tr><td>Daniel Koh</td><td>A</td></tr><tr><td>Priya Nair</td><td>A</td></tr><tr><td>Marcus Ong</td><td>A</td></tr><tr><td>Jia Hui Lee</td><td>A</td></tr><tr><td>Aaron Goh</td><td>A</td></tr><tr><td>Nicole Chua</td><td>A</td></tr><tr><td>Ethan Wee</td><td>A</td></tr><tr><td>Sarah Lim</td><td>A</td></tr><tr><td>Kevin Ho</td><td>A</td></tr><tr><td>Mei Ling Sim</td><td>A</td></tr><tr><td>Jonas Yeo</td><td>A</td></tr><tr><td>Clara Teo</td><td>A</td></tr><tr><td>Ryan Seah</td><td>A</td></tr><tr><td>Amanda Poh</td><td>A</td></tr><tr><td>Wei Jie Low</td><td>A</td></tr><tr><td>Hannah Ng</td><td>A</td></tr><tr><td>Bryan Tay</td><td>A</td></tr><tr><td>Grace Foo</td><td>A</td></tr><tr><td>Ivan Chew</td><td>A</td></tr><tr><td>Zoe Kwek</td><td>A</td></tr><tr><td>Shawn Pang</td><td>A</td></tr><tr><td>Alicia Heng</td><td>A</td></tr>
  </tbody></table>
  <table class="results" style="left:120px"><tbody>
    <tr><td>Joel Quek</td><td>A</td></tr><tr><td>Vanessa Ang</td><td>A</td></tr><tr><td>Benjamin Toh</td><td>A</td></tr><tr><td>Chloe Yap</td><td>A</td></tr><tr><td>Darren Soh</td><td>A</td></tr><tr><td>Eunice Lau</td><td>A</td></tr><tr><td>Farhan Ali</td><td>A</td></tr><tr><td>Gwen Tio</td><td>A</td></tr><tr><td>Isaac Loh</td><td>A</td></tr><tr><td>Jasmine Kee</td><td>A</td></tr><tr><td>Lucas Chan</td><td>A</td></tr><tr><td>Megan Sng</td><td>A</td></tr><tr><td>Nathan Liew</td><td>A</td></tr><tr><td>Olivia Kang</td><td>A</td></tr><tr><td>Paul Chia</td><td>A</td></tr><tr><td>Qi Xuan Ho</td><td>A</td></tr><tr><td>Rui En Tan</td><td>A</td></tr><tr><td>Samuel Lee</td><td>A</td></tr><tr><td>Tricia Wong</td><td>A</td></tr><tr><td>Victor Lum</td><td>A</td></tr><tr><td>Wen Hui Ong</td><td>A</td></tr><tr><td>Xavier Lim</td><td>A</td></tr><tr><td>Yvonne Koh</td><td>A</td></tr>
  </tbody></table>
  <table class="results" style="left:228px"><tbody>
    <tr><td>Adeline Goh</td><td>B</td></tr><tr><td>Brandon Ng</td><td>B</td></tr><tr><td>Cheryl Tan</td><td>B</td></tr><tr><td>Dylan Yeo</td><td>B</td></tr><tr><td>Elaine Sim</td><td>B</td></tr><tr><td>Felix Teo</td><td>B</td></tr><tr><td>Gillian Ho</td><td>B</td></tr><tr><td>Harris Ong</td><td>B</td></tr><tr><td>Irene Chua</td><td>B</td></tr><tr><td>Jared Koh</td><td>B</td></tr><tr><td>Kimberly Lee</td><td>B</td></tr><tr><td>Leon Tay</td><td>B</td></tr><tr><td>Michelle Poh</td><td>B</td></tr><tr><td>Nigel Seah</td><td>B</td></tr><tr><td>Phoebe Foo</td><td>B</td></tr><tr><td>Russell Chew</td><td>B</td></tr><tr><td>Stella Low</td><td>B</td></tr><tr><td>Terence Pang</td><td>B</td></tr><tr><td>Ursula Heng</td><td>B</td></tr><tr><td>Vincent Kwek</td><td>B</td></tr><tr><td>Wendy Quek</td><td>B</td></tr><tr><td>Yusuf Rahim</td><td>B</td></tr><tr><td>Zara Lim</td><td>B</td></tr>
  </tbody></table>

  <div class="cover-foot">
    <p style="left:14px">Mr Lim's lessons are engaging and well structured. His notes are concise and his essay frameworks helped me secure an A. I strongly recommend his classes to every JC student.</p>
    <p style="left:178px">I was failing Economics in JC1, but after joining the programme I improved steadily and scored a distinction. Thank you for your patience and care!</p>
    <span class="tag dark" style="left:14px">Rachel Tan | Harbourview JC</span>
    <span class="tag dark" style="left:228px;font-size:7.5px">Testimonials of Students</span>
  </div>
</section>

<!-- Back page -->
<section class="page back" aria-label="Class schedule, locations and fees">
  <div class="back-band"></div>
  <div class="photo" style="left:22px;top:22px;width:296px;height:120px" role="img" aria-label="Group of students in school uniform"></div>

  <span class="tag dark" style="left:128px;top:158px">Class Schedule*</span>
  <table class="sched" style="left:14px"><tbody>
    <tr><td>JC2 Monday</td><td>5pm</td><td>Riverside</td></tr>
    <tr><td>JC2 Tuesday</td><td>7pm</td><td>Eastbay</td></tr>
    <tr><td>JC1 Tuesday</td><td>7:30pm</td><td>Westfield</td></tr>
    <tr><td>JC2 Wednesday</td><td>7:30pm</td><td>Westfield</td></tr>
    <tr><td>JC1 Wednesday</td><td>6pm</td><td>Eastbay</td></tr>
    <tr><td>JC2 Thursday</td><td>6pm</td><td>Maple Grove</td></tr>
    <tr><td>JC1 Thursday</td><td>7:30pm</td><td>Maple Grove</td></tr>
  </tbody></table>
  <table class="sched" style="left:178px"><tbody>
    <tr><td>JC2 Saturday</td><td>10am</td><td>Maple Grove</td></tr>
    <tr><td>JC2 Saturday</td><td>12pm</td><td>Maple Grove</td></tr>
    <tr><td>JC1 Saturday</td><td>2pm</td><td>Maple Grove</td></tr>
    <tr><td>JC2 Saturday</td><td>4pm</td><td>Maple Grove</td></tr>
    <tr><td>JC2 Sunday</td><td>10am</td><td>Maple Grove</td></tr>
    <tr><td>JC1 Sunday</td><td>12pm</td><td>Maple Grove</td></tr>
    <tr><td>JC2 Sunday</td><td>4pm</td><td>Maple Grove</td></tr>
  </tbody></table>
  <p class="txt" style="position:absolute;left:14px;top:264px;font-size:5px">*MOST classes are already full, call/SMS/message us at 81550247 to confirm available timings.</p>

  <span class="tag" style="left:130px;top:287px;font-size:9px">Our Locations</span>
  <div class="locations">
    <div class="loc"><h4>Maple Grove:</h4><p>Blk 12 Maple Grove Ave #01-20,<br>S680012<br>2 minutes walk from MRT</p></div>
    <div class="loc"><h4>Eastbay:</h4><p>Blk 45 Eastbay North St #01-08<br>(2nd storey), S460045<br>7 minutes walk from MRT</p></div>
    <div class="loc"><h4>Westfield:</h4><p>Blk 38 Westfield Ave 2 #01-11,<br>S120038<br>5 min bus ride from MRT</p></div>
    <div class="loc"><h4>Riverside:</h4><p>Riverside Drive (along Riverside<br>Ave 5, opposite petrol station)<br>5 min bus ride from JC</p></div>
  </div>

  <span class="tag dark" style="left:118px;top:388px;font-size:9px">Fees &amp; Promotions</span>
  <div class="fees">
    <div class="line" style="margin-top:2px">$295 per month – JC2s</div>
    <div class="line">$280 per month – JC1s (early bird promotion)</div>
    <div class="line">Sign up with a friend(s) to enjoy $20 off monthly fees.</div>
    <div class="line" style="margin-top:6px">Sign up now / Contact Us</div>
    <div class="call">Text/Call/Message us at <b>81550247</b></div>
  </div>
</section>

</body>
</html>
```